Customer Dashboard Design for Email Security SaaS

Mailvarden is a commercial email spam filter offered as a SaaS product, built and operated by a small German hosting provider. It protects business email accounts against spam, phishing, scam, and viruses using a multilayer filtering pipeline that combines traditional spam detection with AI-powered classification. The product runs entirely on German infrastructure, ensuring data sovereignty for European customers.

We need a complete redesign of the customer-facing dashboard. This is the web application where paying customers manage their email filtering: view their mail log, check quarantined emails, manage allow/blocklists, configure their settings, and handle their subscription. It is the primary touchpoint between Mailvarden and its customers.

Our customers are system administrators, IT managers at small-to-medium businesses, and operators of small hosting providers. They are technically competent but not designers. They expect professional, efficient tools that respect their time. They typically manage 10–500 email accounts and check the dashboard a few times per week, with heavier use during spam incidents.

We have attached the current mockups which really need to be replaced with something good looking.

Target Market(s)

System administrators, IT managers at small-to-medium businesses, and operators of small hosting providers.

Industry/Entity Type

SaaS

Number of Pages Required

5+ page

```html
<!DOCTYPE html>
<html lang="de">
<head>
<meta charset="utf-8">
<title>Mailvarden Dashboard</title>
<link rel="stylesheet" href="https://fonts.googleapis.com/css2?family=Outfit:wght@400;500;600;700&display=swap">
<style>
:root{
  --stage:#ecebe8;
  --panel:#131213;
  --sidebar:#1b1a1b;
  --line:#3a393b;
  --green:#069a6b;
  --green-deep:#0a5a3f;
  --card:#1e1d1f;
  --row:#262527;
  --field:#2a292b;
  --text:#ffffff;
  --muted:#b9b8ba;
  --red:#e02424;
  --yellow:#f2d21b;
  --grey:#4a494b;
}
*{box-sizing:border-box;margin:0;padding:0}
html,body{width:1200px;height:895px;overflow:hidden}
body{background:linear-gradient(180deg,#e4e3e0,#f1f0ee 60%,#ebeae7);font-family:"Outfit",sans-serif;color:var(--text);position:relative}
.panel{position:absolute;width:531px;height:369px;background:var(--panel);overflow:hidden;box-shadow:0 4px 14px rgba(0,0,0,.12)}
.p1{left:56px;top:59px}.p2{left:613px;top:59px}.p3{left:56px;top:467px}.p4{left:613px;top:467px}
.sidebar{position:absolute;left:0;top:0;width:132px;height:100%;background:var(--sidebar);border-right:1px solid var(--line)}
.brand{position:absolute;left:15px;top:17px;display:flex;align-items:center;gap:6px;font-size:10px;font-weight:500}
.brand-mark{width:18px;height:18px;border-radius:4px;background:var(--green)}
.nav{position:absolute;top:51px;left:0;width:132px;list-style:none}
.nav li{height:24.5px;line-height:22px;padding-left:37px;font-size:7.6px}
.nav li.active{background:var(--green)}
.side-divider{position:absolute;left:10px;top:265px;width:112px;border-top:1px solid var(--line)}
.side-label{position:absolute;left:14px;top:281px;font-size:6.6px;color:var(--muted);letter-spacing:.2px}
.side-admin{position:absolute;left:14px;top:296px;font-size:7.6px}
.main{position:absolute;left:132px;top:0;right:0;bottom:0}
.title{position:absolute;left:28px;top:21px;font-size:15px;font-weight:700}
.lead{position:absolute;left:28px;top:41px;width:300px;font-size:7px;line-height:11px}
.stat{position:absolute;top:66px;height:54px;border-radius:4px;background:var(--card);padding:8px 12px}
.stat.hi{background:var(--green)}
.stat-label{font-size:7px}
.stat-num{font-size:18px;font-weight:700;line-height:18px;margin-top:1px}
.stat-sub{font-size:6.5px;margin-top:2px}
.h2{position:absolute;left:28px;font-size:11px;font-weight:500}
.chart{position:absolute;left:28px;top:160px;width:327px;height:166px;border-radius:6px;background:var(--card)}
.chart svg{position:absolute;left:0;top:0}
.legend{position:absolute;left:15px;top:115px;display:flex;gap:10px;font-size:4.4px}
.legend span{display:flex;align-items:center;gap:3px}
.legend i{width:6px;height:6px;border-radius:1px;display:inline-block}
.link{position:absolute;left:14px;top:141px;font-size:6.6px;color:var(--green)}
.filter{position:absolute;left:8px;top:89px;width:382px;height:73px;border-radius:8px;background:var(--green-deep)}
.filter-title{position:absolute;left:20px;top:13px;font-size:11px;font-weight:700}
.filter-label{position:absolute;top:40px;font-size:7.6px;font-weight:700}
.select{position:absolute;top:35px;width:119px;height:21px;border:1px solid #9fc8b8;border-radius:11px;font-size:5.4px;line-height:19px;padding-left:12px}
.select::after{content:"▾";position:absolute;right:9px;font-size:6px}
.log{position:absolute;left:8px;top:169px;width:382px;height:178px;border-radius:8px;background:var(--row);overflow:hidden}
.log-head,.log-row{position:absolute;left:0;width:100%;height:20px;font-size:5.4px}
.log-head{top:0;height:29px;background:var(--green);font-size:7px}
.log-head span,.log-row span{position:absolute;top:50%;transform:translateY(-50%)}
.c1{left:14px}.c2{left:94px}.c3{left:187px}.c4{left:269px}.c5{left:336px}
.pill{background:#17372b;border-radius:6px;padding:3px 8px;color:#dfeee7}
.banner{position:absolute;left:8px;top:89px;width:382px;height:53px;border-radius:8px;background:var(--green-deep)}
.banner-check{position:absolute;left:20px;top:13px}
.banner-title{position:absolute;left:57px;top:13px;font-size:11px;font-weight:700}
.banner-sub{position:absolute;left:57px;top:28px;font-size:7px}
.field{position:absolute;left:8px;width:382px;height:23px;border-radius:12px;background:var(--field);font-size:5.6px;line-height:23px}
.field-text{position:absolute;left:19px}
.btn{position:absolute;right:0;top:0;width:81px;height:23px;border-radius:12px;background:var(--green);text-align:center;font-size:7px;line-height:23px}
.btn-outline{position:absolute;right:3px;top:2px;width:65px;height:19px;border-radius:10px;border:1px solid #0b5b40;color:var(--green);text-align:center;font-size:7px;line-height:17px}
.type-select{position:absolute;left:0;top:0;width:78px;height:23px;border-radius:12px;border:1px solid #444;padding-left:14px}
.type-select::after{content:"▾";position:absolute;right:9px;font-size:6px}
.hint{position:absolute;left:22px;top:139px;font-size:5.4px}
.hint::before{content:"▶";color:var(--green);margin-right:3px;font-size:5px}
</style>
</head>
<body>

<!-- Overview -->
<section class="panel p1">
  <aside class="sidebar">
    <div class="brand"><span class="brand-mark"></span>Mailvarden</div>
    <ul class="nav"><li class="active">Ubersicht</li><li>Mail-Log</li><li>Postfacher</li><li>Allowlist</li><li>Blocklist</li><li>Quarantane</li><li>Einstellungen</li><li>Abrechnung</li></ul>
    <div class="side-divider"></div><div class="side-label">VERWALTUNG</div><div class="side-admin">Administration</div>
  </aside>
  <div class="main">
    <h1 class="title">Guten Tag</h1>
    <p class="lead">Beobachtungsmodus - Mails werden analysiert aber nicht blockiert</p>
    <div class="stat hi" style="left:28px;width:132px"><div class="stat-label">Letzte 24 Stunden</div><div class="stat-num">0</div><div class="stat-sub">0 zugestellt, 0 abgefangen</div></div>
    <div class="stat" style="left:166px;width:92px"><div class="stat-label">7 TAGE</div><div class="stat-num">0</div><div class="stat-sub">0% zugestellt</div></div>
    <div class="stat" style="left:263px;width:92px"><div class="stat-label">30 TAGE</div><div class="stat-num">0</div><div class="stat-sub">0% zugestellt</div></div>
    <h2 class="h2" style="top:134px">Letzte 30 Tage</h2>
    <div class="chart">
      <svg width="327" height="110" viewBox="0 0 327 110" font-family="Outfit, sans-serif" font-size="5" fill="#fff">
        <g stroke="#3a393b" stroke-width=".6"><line x1="60" y1="28" x2="297" y2="28"/><line x1="60" y1="54" x2="297" y2="54"/><line x1="60" y1="80" x2="297" y2="80"/></g>
        <text x="49" y="30">10</text><text x="49" y="56">5</text><text x="49" y="82">0</text>
        <text x="177" y="95" text-anchor="middle">13.04</text>
      </svg>
      <div class="legend">
        <span><i style="background:var(--green)"></i>Akzeptiert</span>
        <span><i style="background:var(--red)"></i>Abgelehnt</span>
        <span><i style="background:var(--yellow)"></i>Quarantane</span>
        <span><i style="background:var(--grey)"></i>Tempfail</span>
      </div>
      <div class="link">Datentabelle anzeigen</div>
    </div>
  </div>
</section>

<!-- Mail log -->
<section class="panel p2">
  <aside class="sidebar">
    <div class="brand"><span class="brand-mark"></span>Mailvarden</div>
    <ul class="nav"><li>Ubersicht</li><li class="active">Mail-Log</li><li>Postfacher</li><li>Allowlist</li><li>Blocklist</li><li>Quarantane</li><li>Einstellungen</li><li>Abrechnung</li></ul>
    <div class="side-divider"></div><div class="side-label">VERWALTUNG</div><div class="side-admin">Administration</div>
  </aside>
  <div class="main">
    <h1 class="title" style="top:18px">Mail - Log</h1>
    <p class="lead" style="top:39px;width:290px">Hier sehen Sie alle eingehenden E-Mails, die Mailvarden verarbeitet hat. Sie konnen nach Aktion und kategorie filtern, um z. nur abgelehnte oder als Spam erkannte Nachrichten anzuzeigen.</p>
    <div class="filter">
      <div class="filter-title">Filter</div>
      <div class="filter-label" style="left:20px">Aktion</div>
      <div class="select" style="left:48px">Alle Aktionen</div>
      <div class="filter-label" style="left:180px">Kategorie</div>
      <div class="select" style="left:222px">Alle Aktionen</div>
    </div>
    <div class="log">
      <div class="log-head"><span class="c1">Zeit</span><span class="c2">Absender-Domain</span><span class="c3">Aktion</span><span class="c4">Kategorie</span><span class="c5">Score</span></div>
      <div class="log-row" style="top:37px"><span class="c1">13.4.2026, 15:12:58</span><span class="c2">www.postbeispiel.de</span><span class="c3 pill">Akzeptiert</span><span class="c4">Newsletter</span><span class="c5">25.6</span></div>
      <div class="log-row" style="top:58px"><span class="c1">13.4.2026, 15:12:58</span><span class="c2">www.postbeispiel.de</span><span class="c3 pill">Akzeptiert</span><span class="c4">Newsletter</span><span class="c5">25.6</span></div>
      <div class="log-row" style="top:80px"><span class="c1">13.4.2026, 15:12:58</span><span class="c2">www.postbeispiel.de</span><span class="c3 pill">Akzeptiert</span><span class="c4">Newsletter</span><span class="c5">25.6</span></div>
      <div class="log-row" style="top:102px"><span class="c1">13.4.2026, 15:12:58</span><span class="c2">www.postbeispiel.de</span><span class="c3 pill">Akzeptiert</span><span class="c4">Newsletter</span><span class="c5">25.6</span></div>
      <div class="log-row" style="top:125px"><span class="c1">13.4.2026, 15:12:58</span><span class="c2">www.postbeispiel.de</span><span class="c3 pill">Akzeptiert</span><span class="c4">Newsletter</span><span class="c5">25.6</span></div>
      <div class="log-row" style="top:147px"><span class="c1">13.4.2026, 15:12:58</span><span class="c2">www.postbeispiel.de</span><span class="c3 pill">Akzeptiert</span><span class="c4">Newsletter</span><span class="c5">25.6</span></div>
    </div>
  </div>
</section>

<!-- Mailboxes -->
<section class="panel p3">
  <aside class="sidebar">
    <div class="brand"><span class="brand-mark"></span>Mailvarden</div>
    <ul class="nav"><li>Ubersicht</li><li>Mail-Log</li><li class="active">Postfacher</li><li>Allowlist</li><li>Blocklist</li><li>Quarantane</li><li>Einstellungen</li><li>Abrechnung</li></ul>
    <div class="side-divider"></div><div class="side-label">VERWALTUNG</div><div class="side-admin">Administration</div>
  </aside>
  <div class="main">
    <h1 class="title" style="top:20px">Postfacher</h1>
    <p class="lead" style="top:40px;width:300px">Jade E-Mail-Adresse, die Mailvarden schuetzt, belegt einen Platz in Ihrem kontingent. Adressen konnen Sie jederzeit entfernen - der Platz wird sofort frei. Plus-Varianten wie name+tag@firma.example zahlen als</p>
    <div class="banner">
      <svg class="banner-check" width="27" height="27" viewBox="0 0 27 27"><circle cx="13.5" cy="13.5" r="13.5" fill="#0e6a4a"/><path d="M8.5 14l3.5 3.5 6.5-7.5" fill="none" stroke="#fff" stroke-width="2" stroke-linecap="round" stroke-linejoin="round"/></svg>
      <div class="banner-title">kein Postfach-Limit</div>
      <div class="banner-sub">Ihr Tarif hat kein Adress-Limit.Alle eingehenden Mails werden gefiltert.</div>
    </div>
    <h2 class="h2" style="top:157px;font-size:9px;font-weight:700">Adresse hinzufugen</h2>
    <div class="field" style="top:177px"><span class="field-text">nutzer@firma-beispiel.de</span><span class="btn">Hinzufugen</span></div>
    <h2 class="h2" style="top:216px;font-size:9px;font-weight:700">Geschutzte Adressen(1)</h2>
    <div class="field" style="top:236px"><span class="field-text">Manuell hinzugefugt</span><span class="btn-outline">Entfernen</span></div>
  </div>
</section>

<!-- Allowlist -->
<section class="panel p4">
  <aside class="sidebar">
    <div class="brand"><span class="brand-mark"></span>Mailvarden</div>
    <ul class="nav"><li>Ubersicht</li><li>Mail-Log</li><li>Postfacher</li><li class="active">Allowlist</li><li>Blocklist</li><li>Quarantane</li><li>Einstellungen</li><li>Abrechnung</li></ul>
    <div class="side-divider"></div><div class="side-label">VERWALTUNG</div><div class="side-admin">Administration</div>
  </aside>
  <div class="main">
    <h1 class="title" style="top:20px">Allowlist</h1>
    <p class="lead" style="top:40px;width:300px">Absender auf der Allowlist werden vom Spamfilter nicht blockiert. Nautzen Sie diese Liste fur Geschaftspartner. Lieferanten oder Dienste, deren E-Mails immer zugestellt werden sollen.</p>
    <h2 class="h2" style="top:86px;font-size:9px;font-weight:700">Eintrag hinzufugen</h2>
    <div class="field" style="top:106px"><span class="type-select">Absender-Domain</span><span class="field-text" style="left:92px">z.B. lieferant.example</span><span class="btn">Hinzufugen</span></div>
    <div class="hint">Was bedeuten die Eintragstypen?</div>
  </div>
</section>

</body>
</html>
```